Business Card Design for Occupational Medicine Start Up Company

We need to design a professional business card. We are a healthcare company providing occupational medicine services to blue collar industries. We are professional, efficient and high quality service providers.

Target Market(s)

Blue Collar Industry: Shipbuilding, Ports, Trucking Companies; The Executives and Safety Officers for these companies

Industry/Entity Type

Healthcare

Contact Information for Business Card

Logo, Name, Title, Email, Phone

Other font styles liked:
• Please match our Brand Guide

Requirements
Must have
• Our Company Colors and Logo

```html
<!DOCTYPE html>
<html lang="en">
<head>
<meta charset="utf-8">
<title>CrewWell Business Cards</title>
<link href="https://fonts.googleapis.com/css2?family=Montserrat:wght@500;700&display=swap" rel="stylesheet">
<style>
  :root {
    --stage: #9b9b9b;
    --navy: #2a3589;
    --indigo: #3c4f9f;
    --royal: #2a6db5;
    --sky: #29a4dc;
    --sky-light: #45b0e0;
    --amber: #f5a93b;
    --white: #ffffff;
  }
  * { margin: 0; padding: 0; box-sizing: border-box; }
  html, body {
    width: 1200px;
    height: 1056px;
    overflow: hidden;
    background: var(--stage);
    font-family: "Montserrat", sans-serif;
  }
  .sheet {
    width: 1200px;
    height: 1056px;
    display: flex;
    flex-direction: column;
    align-items: center;
    justify-content: center;
    gap: 56px;
  }
  .card {
    position: relative;
    width: 700px;
    height: 400px;
    overflow: hidden;
    box-shadow: 0 18px 40px rgba(0, 0, 0, 0.35);
  }
  .card-front {
    background: linear-gradient(100deg, var(--indigo) 0%, var(--royal) 45%, var(--sky) 100%);
  }
  .card-back {
    background: linear-gradient(100deg, var(--sky) 0%, var(--royal) 60%, var(--indigo) 100%);
  }
  .brand {
    display: flex;
    align-items: center;
    gap: 18px;
    color: var(--navy);
    font-weight: 700;
    letter-spacing: 0.04em;
    text-transform: uppercase;
  }
  .brand-dot {
    border-radius: 50%;
    background: var(--navy);
    flex: none;
  }
  .card-front .brand {
    position: absolute;
    top: 48px;
    left: 80px;
    font-size: 52px;
  }
  .card-front .brand-dot { width: 72px; height: 72px; }
  .accent-rule {
    position: absolute;
    left: 0;
    right: 0;
    top: 152px;
    height: 7px;
    background: var(--amber);
    box-shadow: 0 3px 6px rgba(20, 30, 90, 0.35);
  }
  .contact {
    position: absolute;
    left: 200px;
    top: 196px;
    color: var(--white);
  }
  .contact-name {
    font-size: 28px;
    font-weight: 700;
    letter-spacing: 0.14em;
    margin-bottom: 22px;
  }
  .contact-line {
    font-size: 18px;
    font-weight: 500;
    letter-spacing: 0.12em;
    line-height: 1.5;
  }
  .card-back .brand {
    position: absolute;
    inset: 0;
    justify-content: center;
    font-size: 58px;
  }
  .card-back .brand-dot { width: 84px; height: 84px; }
</style>
</head>
<body>
  <main class="sheet">
    <section class="card card-front" aria-label="Business card front">
      <div class="brand">
        <span class="brand-dot"></span>
        <span class="brand-name">CrewWell</span>
      </div>
      <div class="accent-rule"></div>
      <div class="contact">
        <p class="contact-name">Title Full Name</p>
        <p class="contact-line">full.name@crewwell.com</p>
        <p class="contact-line">123-456-7890</p>
      </div>
    </section>
    <section class="card card-back" aria-label="Business card back">
      <div class="brand">
        <span class="brand-dot"></span>
        <span class="brand-name">CrewWell</span>
      </div>
    </section>
  </main>
</body>
</html>
```